Web form face-lift for an online startup

We are a web startup building a SaaS application for the freight industry. The project is mainly dedicated to the paint the main form that our customer are using along the search results that the they get. All details are in the attached documents.
Updates
The application serves the Freight Forwarders community so please think towards this industry when using background images, banners, colors, icons, etc. Computer and technology images are irrelevant.
Customer fields at the top of the page is actually part of the form.
Target Market(s)
Usually business users (Sales people, procurement, shippers, freight forwarders). Some are less tech savvy and some appreciate the new trendy web apps.
Industry/Entity Type
Building
Colors
Designer to choose colors to be used in the design.
Look and feel
Each slider illustrates characteristics of the customer's brand and the style your logo design should communicate.

```html
<!DOCTYPE html>
<html lang="en">
<head>
<meta charset="utf-8">
<title>Sample data table</title>
<link href="https://fonts.googleapis.com/css2?family=Montserrat:wght@400;500;600&family=Lato:wght@400;700&display=swap" rel="stylesheet">
<style>
:root{
  --topbar:#1f2427;
  --topbar-text:#b9bec2;
  --band-dark:#0b5ca6;
  --band-light:#1b9be0;
  --accent:#f07c1e;
  --page:#e8e8e8;
  --ink:#222;
  --muted:#555;
  --line:#cfcfcf;
  --row-alt:#f2f2f2;
  --row:#ffffff;
  --btn:#1561b8;
  --btn-dark:#0d4b94;
  --icon-blue:#2a73c8;
  --icon-orange:#d08a2e;
  --icon-red:#d0281e;
  --footer:#3b3b3b;
}
*{box-sizing:border-box;margin:0;padding:0}
html,body{width:1200px;height:760px;overflow:hidden}
body{position:relative;background:var(--page);font-family:"Lato",sans-serif;color:var(--ink)}

.topbar{position:absolute;left:0;top:0;width:1200px;height:32px;background:var(--topbar);border-bottom:1px solid #2c83c9;font-family:"Lato",sans-serif;font-size:9px;color:var(--topbar-text);letter-spacing:.2px}
.topbar .nav{position:absolute;left:124px;top:0;height:32px;display:flex;align-items:center;gap:19px}
.topbar .nav span,.topbar .account span{display:flex;align-items:center;gap:5px}
.topbar svg{fill:var(--topbar-text)}
.topbar .lang{position:absolute;left:868px;top:0;height:32px;display:flex;align-items:center;gap:4px}
.flag{width:10px;height:7px;background:linear-gradient(#c33 0 50%,#eee 50%);position:relative}
.flag::before{content:"";position:absolute;left:0;top:0;width:5px;height:4px;background:#335}
.topbar .account{position:absolute;right:122px;top:0;height:32px;display:flex;align-items:center;gap:16px}

.masthead{position:absolute;left:0;top:33px;width:1200px;height:71px;background:linear-gradient(90deg,var(--band-dark),var(--band-light) 55%,var(--band-dark))}
.brand{position:absolute;left:127px;top:22px;font-family:"Montserrat",sans-serif;font-weight:500;font-size:20px;color:#fff;letter-spacing:-.5px}
.divider{position:absolute;left:257px;top:21px;width:1px;height:27px;background:rgba(255,255,255,.55)}
.tagline{position:absolute;left:274px;top:26px;font-family:"Lato",sans-serif;font-size:14px;color:#cfe6f7}
.menu{position:absolute;left:566px;top:0;height:71px;display:flex;align-items:center;font-family:"Montserrat",sans-serif;font-weight:500;font-size:11.5px;color:#fff}
.menu svg{margin-right:14px}
.menu a{color:#fff;text-decoration:none;margin-right:31px}
.menu a:last-child{margin-right:0}

.page-title{position:absolute;left:120px;top:128px;font-family:"Montserrat",sans-serif;font-weight:400;font-size:24.5px;color:#111}
.search{position:absolute;left:120px;top:174px;display:flex;align-items:center}
.search label{font-family:"Montserrat",sans-serif;font-size:14px;color:#444;margin-right:7px}
.search .field{width:181px;height:29px;background:#fff;border:1px solid #d8d8d8}
.search .button{width:86px;height:29px;background:linear-gradient(var(--btn),var(--btn-dark));color:#fff;font-family:"Montserrat",sans-serif;font-weight:500;font-size:11px;display:flex;align-items:center;justify-content:center;border-bottom:2px solid #0a3b78}

.orders{position:absolute;left:120px;top:219px;width:960px;border-collapse:collapse;table-layout:fixed;font-size:11.5px}
.orders th,.orders td{border:1px solid var(--line)}
.orders th{height:39px;background:#fff;font-family:"Montserrat",sans-serif;font-weight:400;font-size:13px;color:#333;text-align:center}
.orders td{height:27.2px;padding-left:15px;color:#222}
.orders td.num{padding-left:0;text-align:center}
.orders tr:nth-child(odd) td{background:var(--row-alt)}
.orders tr:nth-child(even) td{background:var(--row)}
.orders td.actions{padding-left:12px}
.actions svg{vertical-align:middle;margin-right:7px}

.pager{position:absolute;right:120px;top:647px;display:flex;gap:5px;font-size:9px}
.pager span{height:17px;padding:0 5px;min-width:17px;display:flex;align-items:center;justify-content:center;background:#fff;border:1px solid #c8c8c8;color:#333}
.pager .off{color:#c8c8c8;border-color:#e2e2e2}
.pager .current{background:var(--btn);border-color:var(--btn-dark);color:#fff}
.pager .gap{margin-left:2px}

.footer{position:absolute;left:0;top:722px;width:1200px;height:38px;background:var(--footer);font-family:"Montserrat",sans-serif;font-weight:500;font-size:11.5px;color:#fff}
.footer .links{position:absolute;left:122px;top:0;height:38px;display:flex;align-items:center;gap:15px}
.footer .sep{color:#ddd}
.footer .social{position:absolute;right:128px;top:0;height:38px;display:flex;align-items:center;gap:12px}
.footer .social span{width:16px;height:16px;border-radius:50%;background:#fff}
</style>
</head>
<body>

<header class="topbar">
  <div class="nav">
    <span><svg width="11" height="9" viewBox="0 0 11 9"><path d="M5.5 0 11 4.5H9.5V9H7V6H4v3H1.5V4.5H0z"/></svg>HOME</span>
    <span><svg width="10" height="10" viewBox="0 0 10 10"><path d="M4.3 0h1.4v3.5L10 6v1.2L5.7 5.8V8.3L7 9.3V10L5 9.4 3 10v-.7l1.3-1V5.8L0 7.2V6l4.3-2.5z"/></svg>FLIGHTS</span>
    <span><svg width="10" height="10" viewBox="0 0 10 10"><path d="M0 0h10v10H6V7H4v3H0zm2 2v2h2V2zm4 0v2h2V2z"/></svg>HOTELS</span>
    <span><svg width="13" height="10" viewBox="0 0 13 10"><path d="M0 2l4-2 5 2 4-2v8l-4 2-5-2-4 2zm1 .6v5.8l3-1.5V1.1zm4-1.5v5.8l3 1.2V2.3zm4 1.3v5.8l3-1.5V1.4z"/></svg>MORE</span>
  </div>
  <div class="lang">ENGLISH <span class="flag"></span><svg width="7" height="4" viewBox="0 0 7 4"><path d="M0 0h7L3.5 4z"/></svg></div>
  <div class="account">
    <span><svg width="7" height="9" viewBox="0 0 7 9"><path d="M1.2 4V2.4a2.3 2.3 0 0 1 4.6 0V4H7v5H0V4zm1.2 0h2.2V2.4a1.1 1.1 0 0 0-2.2 0z"/></svg>LOGIN</span>
    <span><svg width="10" height="10" viewBox="0 0 10 10"><circle cx="5" cy="3" r="2.6"/><path d="M0 10c0-3 2-4.4 5-4.4s5 1.4 5 4.4z"/></svg>SIGNUP</span>
  </div>
</header>

<section class="masthead">
  <div class="brand">FREIGHTDESK</div>
  <div class="divider"></div>
  <div class="tagline">Tag Line Place here</div>
  <nav class="menu">
    <svg width="25" height="15" viewBox="0 0 25 15" fill="none" stroke="#f07c1e" stroke-width="2.4"><path d="M2 14a10.5 10.5 0 0 1 21 0z"/><path d="M12.5 14 17 7"/></svg>
    <a>Menu item 1</a><a>Menu item 2</a><a>Menu item 3</a><a>Menu item 4</a><a>Menu item 5</a>
  </nav>
</section>

<h1 class="page-title">Sample data table</h1>

<form class="search">
  <label>Search by order Bumber</label>
  <div class="field"></div>
  <div class="button">SEARCH</div>
</form>

<table class="orders">
  <colgroup>
    <col style="width:77px"><col style="width:114px"><col style="width:133px"><col style="width:136px"><col style="width:142px"><col style="width:87px"><col style="width:93px"><col style="width:94px"><col style="width:84px">
  </colgroup>
  <thead>
    <tr><th style="text-align:left;padding-left:8px">Order No.</th><th>OrderDate</th><th>Region</th><th>Rep</th><th>Item</th><th>Units</th><th>Cost</th><th>Total</th><th></th></tr>
  </thead>
  <tbody>
    <tr><td class="num">0001</td><td>1/6/2012</td><td>East</td><td>Jones</td><td>Pencil</td><td>95</td><td>1.99</td><td>189.05</td><td class="actions"></td></tr>
    <tr><td class="num">0002</td><td>1/23/2012</td><td>Central</td><td>Kivell</td><td>Binder</td><td>50</td><td>19.99</td><td>999.5</td><td class="actions"></td></tr>
    <tr><td class="num">0003</td><td>2/9/2012</td><td>Central</td><td>Jardine</td><td>Pencil</td><td>36</td><td>4.99</td><td>179.64</td><td class="actions"></td></tr>
    <tr><td class="num">0004</td><td>2/26/2012</td><td>Central</td><td>Gill</td><td>Pen</td><td>27</td><td>19.99</td><td>539.73</td><td class="actions"></td></tr>
    <tr><td class="num">0005</td><td>3/15/2012</td><td>West</td><td>Sorvino</td><td>Pencil</td><td>56</td><td>2.99</td><td>167.44</td><td class="actions"></td></tr>
    <tr><td class="num">0006</td><td>4/1/2012</td><td>East</td><td>Jones</td><td>Binder</td><td>60</td><td>4.99</td><td>299.4</td><td class="actions"></td></tr>
    <tr><td class="num">0007</td><td>4/18/2012</td><td>Central</td><td>Andrews</td><td>Pencil</td><td>75</td><td>1.99</td><td>149.25</td><td class="actions"></td></tr>
    <tr><td class="num">0008</td><td>5/5/2012</td><td>Central</td><td>Jardine</td><td>Pencil</td><td>90</td><td>4.99</td><td>449.1</td><td class="actions"></td></tr>
    <tr><td class="num">0009</td><td>5/22/2012</td><td>West</td><td>Thompson</td><td>Pencil</td><td>32</td><td>1.99</td><td>63.68</td><td class="actions"></td></tr>
    <tr><td class="num">0010</td><td>6/8/2012</td><td>East</td><td>Jones</td><td>Binder</td><td>60</td><td>8.99</td><td>539.4</td><td class="actions"></td></tr>
    <tr><td class="num">0011</td><td>6/25/2012</td><td>Central</td><td>Morgan</td><td>Pencil</td><td>90</td><td>4.99</td><td>449.1</td><td class="actions"></td></tr>
    <tr><td class="num">0012</td><td>7/12/2012</td><td>East</td><td>Howard</td><td>Binder</td><td>29</td><td>1.99</td><td>57.71</td><td class="actions"></td></tr>
    <tr><td class="num">0013</td><td>7/29/2012</td><td>East</td><td>Parent</td><td>Binder</td><td>81</td><td>19.99</td><td>1,619.19</td><td class="actions"></td></tr>
    <tr><td class="num">0014</td><td>8/15/2012</td><td>East</td><td>Jones</td><td>Pencil</td><td>35</td><td>4.99</td><td>174.65</td><td class="actions"></td></tr>
  </tbody>
</table>

<svg width="0" height="0" style="position:absolute">
  <defs>
    <g id="icon-view"><circle cx="5" cy="5" r="3.8" fill="none" stroke="#2a73c8" stroke-width="1.6"/><path d="M7.8 7.8 12 12" stroke="#2a73c8" stroke-width="2"/></g>
    <g id="icon-edit"><rect x="0.7" y="0.7" width="10" height="11.6" fill="#fff6e8" stroke="#d08a2e" stroke-width="1.2"/><path d="M3 4h6M3 6.5h6M3 9h4" stroke="#d08a2e" stroke-width="1"/><path d="M9 12l4-4 1 1-4 4h-1z" fill="#d08a2e"/></g>
    <g id="icon-delete"><rect x="1" y="1" width="10" height="2" fill="#d0281e"/><rect x="4" y="0" width="4" height="1.5" fill="#d0281e"/><path d="M2 4h8l-.8 9H2.8z" fill="#d0281e"/><path d="M4.5 5.5v6M7.5 5.5v6" stroke="#fff" stroke-width=".9"/></g>
  </defs>
</svg>
<style>
.actions{background-image:none}
</style>

<div style="position:absolute;left:1008px;top:266px;width:70px">
  <svg width="70" height="360" viewBox="0 0 70 360">
    <g transform="translate(0,0)"><use href="#icon-view"/><use href="#icon-edit" x="22" y="1"/><use href="#icon-delete" x="46" y="1"/></g>
    <g transform="translate(0,27.2)"><use href="#icon-view"/><use href="#icon-edit" x="22" y="1"/><use href="#icon-delete" x="46" y="1"/></g>
    <g transform="translate(0,54.4)"><use href="#icon-view"/><use href="#icon-edit" x="22" y="1"/><use href="#icon-delete" x="46" y="1"/></g>
    <g transform="translate(0,81.6)"><use href="#icon-view"/><use href="#icon-edit" x="22" y="1"/><use href="#icon-delete" x="46" y="1"/></g>
    <g transform="translate(0,108.8)"><use href="#icon-view"/><use href="#icon-edit" x="22" y="1"/><use href="#icon-delete" x="46" y="1"/></g>
    <g transform="translate(0,136)"><use href="#icon-view"/><use href="#icon-edit" x="22" y="1"/><use href="#icon-delete" x="46" y="1"/></g>
    <g transform="translate(0,163.2)"><use href="#icon-view"/><use href="#icon-edit" x="22" y="1"/><use href="#icon-delete" x="46" y="1"/></g>
    <g transform="translate(0,190.4)"><use href="#icon-view"/><use href="#icon-edit" x="22" y="1"/><use href="#icon-delete" x="46" y="1"/></g>
    <g transform="translate(0,217.6)"><use href="#icon-view"/><use href="#icon-edit" x="22" y="1"/><use href="#icon-delete" x="46" y="1"/></g>
    <g transform="translate(0,244.8)"><use href="#icon-view"/><use href="#icon-edit" x="22" y="1"/><use href="#icon-delete" x="46" y="1"/></g>
    <g transform="translate(0,272)"><use href="#icon-view"/><use href="#icon-edit" x="22" y="1"/><use href="#icon-delete" x="46" y="1"/></g>
    <g transform="translate(0,299.2)"><use href="#icon-view"/><use href="#icon-edit" x="22" y="1"/><use href="#icon-delete" x="46" y="1"/></g>
    <g transform="translate(0,326.4)"><use href="#icon-view"/><use href="#icon-edit" x="22" y="1"/><use href="#icon-delete" x="46" y="1"/></g>
    <g transform="translate(0,353.6)"><use href="#icon-view"/></g>
  </svg>
</div>
<div style="position:absolute;left:1008px;top:620px;width:70px;height:14px">
  <svg width="70" height="14" viewBox="0 0 70 14"><use href="#icon-edit" x="22" y="0"/><use href="#icon-delete" x="46" y="0"/></svg>
</div>

<nav class="pager">
  <span class="off">First</span><span class="off">Previous</span>
  <span class="current gap">1</span><span>2</span><span>3</span><span>4</span><span>5</span>
  <span>Next</span><span>Last</span>
</nav>

<footer class="footer">
  <div class="links">
    <span>Home</span><span class="sep">/</span><span>About us</span><span class="sep">/</span><span>Privacy policy</span><span class="sep">/</span><span>Terms of service</span><span class="sep">/</span><span>News</span>
  </div>
  <div class="social"><span></span><span></span><span></span><span></span><span></span></div>
</footer>

</body>
</html>
```